Gentle Harbor Label

We need labels for a new brewery called "Gentle Harbor":

We need one label, that we can slightly change to suit the style of liquid. So far the beers are:
- XPA
- Pale ALe
- IPA
- Black Ale

We want creative, fun labels, nothing traditional. but appropriate to suit all international markets.

Design was promoted in LOGO & not in Design, so we got a lot of logo's but very little designs for bottles/cans.

Gentle Harbor Brewing

```html
<!DOCTYPE html>
<html lang="en">
<head>
<meta charset="utf-8">
<title>Gentle Harbor Label</title>
<link rel="stylesheet" href="https://fonts.googleapis.com/css2?family=Sancreek&family=Libre+Baskerville&family=Montserrat:wght@700&display=swap">
<style>
  :root {
    --backdrop: #333233;
    --label-dark: #2c2d30;
    --label-mid: #34353a;
    --gold: #dcad45;
    --gold-deep: #a7772a;
    --filigree: #5a4a32;
    --ink-light: #f4efe6;
    --ink-shadow: #1d1d1f;
    --orange: #c85a2e;
    --teal: #2e7878;
    --red: #bd3146;
    --green: #5e8c45;
  }
  * { margin: 0; padding: 0; box-sizing: border-box; }
  html, body { width: 1200px; height: 855px; overflow: hidden; background: var(--backdrop); }
  .label-sheet {
    width: 1200px; height: 855px;
    display: grid;
    grid-template-columns: repeat(2, 290px);
    grid-template-rows: repeat(2, 376px);
    gap: 40px 70px;
    justify-content: center;
    align-content: center;
  }
  .beer-label { width: 290px; height: 376px; display: block; overflow: visible; }
  .label-orange { --accent: var(--orange); }
  .label-teal { --accent: var(--teal); }
  .label-red { --accent: var(--red); }
  .label-green { --accent: var(--green); }
  .premium-text { font-family: "Libre Baskerville", serif; font-size: 22px; fill: var(--ink-light); letter-spacing: 1px; }
  .brand-name { font-family: "Libre Baskerville", serif; font-size: 31px; fill: var(--ink-light); }
  .brand-sub { font-family: "Montserrat", sans-serif; font-weight: 700; font-size: 22px; fill: var(--ink-light); letter-spacing: 4px; }
  .style-name { font-family: "Sancreek", serif; font-size: 92px; fill: var(--ink-light); }
  .style-name-shadow { font-family: "Sancreek", serif; font-size: 92px; fill: var(--ink-shadow); }
  .banner { fill: var(--accent); }
  .banner-stitch { fill: none; stroke: var(--ink-light); stroke-width: 2; stroke-dasharray: 2 5; opacity: .8; }
  .star { fill: var(--accent); }
  .flourish { stroke: var(--ink-light); stroke-width: 2; fill: none; }
  .flourish-dot { fill: var(--ink-light); }
  .filigree-area { fill: url(#filigree-fill); }
</style>
</head>
<body>
<svg width="0" height="0" style="position:absolute" aria-hidden="true">
  <defs>
    <linearGradient id="label-fill" x1="0" y1="0" x2="1" y2="0">
      <stop offset="0" stop-color="var(--label-dark)"/>
      <stop offset=".5" stop-color="var(--label-mid)"/>
      <stop offset="1" stop-color="var(--label-dark)"/>
    </linearGradient>
    <linearGradient id="gold-edge" x1="0" y1="0" x2="1" y2="1">
      <stop offset="0" stop-color="#f3d27a"/>
      <stop offset=".5" stop-color="var(--gold)"/>
      <stop offset="1" stop-color="var(--gold-deep)"/>
    </linearGradient>
    <linearGradient id="filigree-fill" x1="0" y1="0" x2="1" y2="0">
      <stop offset="0" stop-color="var(--filigree)" stop-opacity=".55"/>
      <stop offset=".5" stop-color="var(--filigree)" stop-opacity=".9"/>
      <stop offset="1" stop-color="var(--filigree)" stop-opacity=".55"/>
    </linearGradient>
    <path id="shield-path" d="M60 60 L100 60 Q130 60 140 38 Q210 -12 280 38 Q290 60 320 60 L360 60 L360 88 Q382 94 382 122 L382 440 Q382 468 360 474 L360 500 L322 500 Q300 500 290 518 Q210 568 130 518 Q120 500 98 500 L60 500 L60 474 Q38 468 38 440 L38 122 Q38 94 60 88 Z"/>
    <path id="premium-arc" d="M128 106 Q210 76 292 106"/>
    <path id="brewing-arc" d="M132 490 Q210 536 288 490"/>
    <symbol id="label-frame" viewBox="0 0 420 545">
      <use href="#shield-path" fill="url(#label-fill)" stroke="url(#gold-edge)" stroke-width="7"/>
      <path class="star" d="M210 14 l3 7 7 0 -5.5 4.5 2 7 -6.5-4 -6.5 4 2-7 -5.5-4.5 7 0z"/>
      <path class="star" d="M162 24 l2.5 6 6 0 -4.5 3.5 1.5 6 -5.5-3.5 -5.5 3.5 1.5-6 -4.5-3.5 6 0z"/>
      <path class="star" d="M258 24 l2.5 6 6 0 -4.5 3.5 1.5 6 -5.5-3.5 -5.5 3.5 1.5-6 -4.5-3.5 6 0z"/>
      <path class="star" d="M122 48 l2 5 5 0 -4 3 1.5 5 -4.5-3 -4.5 3 1.5-5 -4-3 5 0z"/>
      <path class="star" d="M298 48 l2 5 5 0 -4 3 1.5 5 -4.5-3 -4.5 3 1.5-5 -4-3 5 0z"/>
      <text class="premium-text" text-anchor="middle"><textPath href="#premium-arc" startOffset="50%">PREMIUM</textPath></text>
      <rect class="filigree-area" x="110" y="122" width="200" height="58" rx="29" role="img" aria-label="Gold filigree ornament above the banner"/>
      <rect class="filigree-area" x="110" y="362" width="200" height="58" rx="29" role="img" aria-label="Gold filigree ornament below the banner"/>
      <text class="brand-name" x="210" y="470" text-anchor="middle" textLength="250" lengthAdjust="spacingAndGlyphs">Gentle Harbor</text>
      <text class="brand-sub" text-anchor="middle"><textPath href="#brewing-arc" startOffset="50%">BREWING</textPath></text>
    </symbol>
    <symbol id="label-banner" viewBox="0 0 420 545">
      <path class="banner" d="M24 196 Q210 160 396 196 Q424 272 396 348 Q210 312 24 348 Q-4 272 24 196 Z"/>
      <path class="banner-stitch" d="M26 208 Q210 174 394 208"/>
      <path class="banner-stitch" d="M26 336 Q210 300 394 336"/>
    </symbol>
  </defs>
</svg>

<main class="label-sheet">
  <svg class="beer-label label-orange" viewBox="0 0 420 545" role="img" aria-label="Black Ale label">
    <use href="#label-frame"/>
    <use href="#label-banner"/>
    <text class="style-name-shadow" x="213" y="306" text-anchor="middle" textLength="370" lengthAdjust="spacingAndGlyphs">BLACK ALE</text>
    <text class="style-name" x="210" y="302" text-anchor="middle" textLength="370" lengthAdjust="spacingAndGlyphs">BLACK ALE</text>
  </svg>

  <svg class="beer-label label-teal" viewBox="0 0 420 545" role="img" aria-label="XPA label">
    <use href="#label-frame"/>
    <use href="#label-banner"/>
    <g class="flourish-group">
      <circle class="flourish-dot" cx="18" cy="272" r="2.5"/><circle class="flourish-dot" cx="28" cy="272" r="2.5"/>
      <line class="flourish" x1="62" y1="272" x2="128" y2="272"/>
      <line class="flourish" x1="292" y1="272" x2="358" y2="272"/>
      <circle class="flourish-dot" cx="392" cy="272" r="2.5"/><circle class="flourish-dot" cx="402" cy="272" r="2.5"/>
    </g>
    <text class="style-name-shadow" x="213" y="306" text-anchor="middle">XPA</text>
    <text class="style-name" x="210" y="302" text-anchor="middle">XPA</text>
  </svg>

  <svg class="beer-label label-red" viewBox="0 0 420 545" role="img" aria-label="Pale Ale label">
    <use href="#label-frame"/>
    <use href="#label-banner"/>
    <text class="style-name-shadow" x="213" y="306" text-anchor="middle" textLength="320" lengthAdjust="spacingAndGlyphs">PALE ALE</text>
    <text class="style-name" x="210" y="302" text-anchor="middle" textLength="320" lengthAdjust="spacingAndGlyphs">PALE ALE</text>
  </svg>

  <svg class="beer-label label-green" viewBox="0 0 420 545" role="img" aria-label="IPA label">
    <use href="#label-frame"/>
    <use href="#label-banner"/>
    <g class="flourish-group">
      <circle class="flourish-dot" cx="18" cy="272" r="2.5"/><circle class="flourish-dot" cx="28" cy="272" r="2.5"/>
      <line class="flourish" x1="62" y1="272" x2="140" y2="272"/>
      <line class="flourish" x1="280" y1="272" x2="358" y2="272"/>
      <circle class="flourish-dot" cx="392" cy="272" r="2.5"/><circle class="flourish-dot" cx="402" cy="272" r="2.5"/>
    </g>
    <text class="style-name-shadow" x="213" y="306" text-anchor="middle">IPA</text>
    <text class="style-name" x="210" y="302" text-anchor="middle">IPA</text>
  </svg>
</main>
</body>
</html>
```